Tarrow Consulting Needs Standardised Stationery!

Hello,I am looking at having some standardised stationery to continue building my brand. I am looking for a relatively clean and simple designs using the colours from my logos. Tarrow Consulting is the main business with Folvane Careers Australia a subsidiary.
In particular I am after a design for:
- Letterhead (very important), white background, professional, corporate that I can send to prospective clients. Logo colours.
- Envelope, standard design I can print onto envelopes.
- Pens
- Other stationery/promotional items I can create

Target Market(s)

Universities, government, large organisations.

Industry/Entity Type

Professional Service

Font styles to use
Serif

Requirements
Must have
• Logo, match the design of the Tarrow Consulting logo. Black Folvane Careers Australia logo is a subsidiary.
Should not have
• Too much colour, some colour is good, but I am looking for a clean professional look.

```html
<!DOCTYPE html>
<html lang="en">
<head>
<meta charset="utf-8">
<title>Tarrow Consulting Letterhead</title>
<link href="https://fonts.googleapis.com/css2?family=Lato:wght@400;700&family=Roboto:wght@400&display=swap" rel="stylesheet">
<style>
  :root {
    --backdrop: #e9e9e9;
    --paper: #ffffff;
    --ink-dark: #222222;
    --ink-body: #6a6a6a;
    --ink-muted: #8a8a8a;
    --rule: #9a9a9a;
    --brand-blue: #1a8bcb;
    --brand-green: #21a355;
    --brand-orange: #e38431;
  }
  html, body {
    margin: 0;
    width: 1200px;
    height: 1200px;
    overflow: hidden;
    background: var(--backdrop);
  }
  .letterhead {
    position: absolute;
    left: 176px;
    top: 0;
    width: 848px;
    height: 1200px;
    background: var(--paper);
    font-family: "Lato", sans-serif;
    color: var(--ink-body);
  }
  .brand {
    position: absolute;
    left: 76px;
    top: 88px;
    display: flex;
    align-items: center;
    gap: 12px;
  }
  .brand-mark {
    width: 14px;
    height: 14px;
    background: var(--brand-blue);
  }
  .brand-name {
    font-family: "Lato", sans-serif;
    font-weight: 400;
    font-size: 26px;
    letter-spacing: 1px;
    color: var(--ink-dark);
  }
  .sender {
    position: absolute;
    left: 621px;
    top: 77px;
    height: 71px;
    padding-left: 20px;
    border-left: 1px solid var(--rule);
    font-family: "Roboto", sans-serif;
    font-size: 10px;
    line-height: 14px;
    color: #444;
  }
  .sender .address { margin-bottom: 6px; }
  .sender .line { display: flex; align-items: center; gap: 5px; }
  .sender svg { width: 7px; height: 7px; }
  .recipient { position: absolute; left: 76px; top: 322px; }
  .recipient .to { font-size: 13px; color: var(--ink-muted); }
  .recipient .name { margin-top: 26px; font-size: 18px; color: var(--ink-muted); }
  .recipient .role { font-size: 11px; color: var(--ink-muted); margin-top: 2px; }
  .recipient .contacts { margin-top: 22px; font-size: 11px; line-height: 18px; color: var(--ink-muted); }
  .recipient .contacts b { font-weight: 400; font-size: 14px; }
  .salutation { position: absolute; left: 76px; top: 511px; font-size: 14px; color: var(--ink-muted); }
  .body-copy { position: absolute; left: 76px; width: 695px; text-align: justify; margin: 0; }
  .intro { top: 549px; font-size: 11px; line-height: 22px; color: #555; }
  .para-two { top: 630px; font-size: 13.5px; line-height: 24px; }
  .para-three { top: 750px; font-size: 13.5px; line-height: 24px; }
  .subsidiary {
    position: absolute;
    left: 73px;
    top: 1112px;
    display: flex;
    align-items: center;
    gap: 8px;
  }
  .subsidiary-mark {
    width: 36px;
    height: 36px;
    border-radius: 50%;
    background: var(--ink-dark);
  }
  .subsidiary-name {
    font-weight: 700;
    font-size: 17px;
    line-height: 20px;
    color: var(--ink-dark);
  }
  .colour-band {
    position: absolute;
    left: 0;
    bottom: 0;
    width: 100%;
    height: 14px;
    display: flex;
  }
  .colour-band span { flex: 1; }
  .band-blue { background: var(--brand-blue); }
  .band-green { background: var(--brand-green); }
  .band-orange { background: var(--brand-orange); }
</style>
</head>
<body>
<main class="letterhead">
  <header>
    <div class="brand">
      <span class="brand-mark"></span>
      <span class="brand-name">Tarrow Consulting</span>
    </div>
    <div class="sender">
      <div class="address">28 Harlow Lane<br>Brookfield, Texas 78011</div>
      <div class="line">
        <svg viewBox="0 0 10 10"><path d="M2 1l2 0 1 2-1 1q1 2 3 3l1-1 2 1 0 2q-5 0-8-8z" fill="var(--brand-blue)"/></svg>
        1-800-555-0142
      </div>
      <div class="line">
        <svg viewBox="0 0 10 10"><rect x="0" y="2" width="10" height="6" fill="var(--brand-green)"/></svg>
        hello@tarrowconsulting.com
      </div>
      <div class="line">
        <svg viewBox="0 0 10 10"><circle cx="5" cy="5" r="4.5" fill="var(--brand-orange)"/></svg>
        www.tarrowconsulting.com
      </div>
    </div>
  </header>

  <section class="recipient">
    <div class="to">To</div>
    <div class="name">Jordan Hale</div>
    <div class="role">Director</div>
    <div class="contacts">
      <b>P:</b> (01) 000 000 0000<br>
      <b>E:</b> jordan@hale-office.com<br>
      www.haleoffice.com
    </div>
  </section>

  <div class="salutation">Dear Sir</div>

  <p class="body-copy intro">Lorem ipsum dolor sit amet, consectetur adipiscing elit. Donec orci purus, luctus vitae dignissim eu, iaculis sed purus. Vivamus faucibus, ipsum nec aliquet viverra, leo mauris condimentum ligula, sit amet sagittis enim ligula quis arcu. Nam egestas tortor id nisi porttitor mattis. In tortor ante, ultricies in suscipit a, tempus non massa. Vivamus et auctor mi. Fusce vel massa null</p>

  <p class="body-copy para-two">Phasellus nec eros mauris, et scelerisque orci. Donec malesuada orci vitae nulla accumsan porta a id massa. Quisque accumsan iaculis magna sit amet fringilla. Maecenas consequat, magna eget tincidunt semper, odio nibh rutrum mi, id feugiat ante nisi eu risus. Vestibulum nunc orci, rhoncus a placerat in, ultricies in mi. Cras mattis varius eros, vel fringilla nisi suscipit eget.</p>

  <p class="body-copy para-three">Quisque scelerisque sagittis nulla at porttitor. Mauris a justo et tellus interdum tristique. Sed id augue vitae urna euismod commodo aliquet a quam. Pellentesque arcu velit, cursus et malesuada. Quisque scelerisque sagittis nulla at porttitor. Mauris a justo et tellus interdum tristique. Sed id augue vitae urna euismod commodo aliquet a quam. Pellentesque arcu velit, cursus et malesuada. Mauris a justo et tellus interdum tristique. Sed id augue vitae urna euismod commodo aliquet a quam. cursus et malesuada. Quisque scelerisque sagittis nulla at porttitor. Mauris a justo et tellus interdum tristique. Sed id augue vitae urna euismod commodo aliquet a quam. Pellentesque arcu velit, cursus et malesuada. Mauris a justo et tellus interdum tristique. Sed id augue vitae urna euismod commodo aliquet a quam.</p>

  <footer>
    <div class="subsidiary">
      <span class="subsidiary-mark"></span>
      <span class="subsidiary-name">Folvane Careers Australia</span>
    </div>
    <div class="colour-band">
      <span class="band-blue"></span>
      <span class="band-green"></span>
      <span class="band-orange"></span>
    </div>
  </footer>
</main>
</body>
</html>
```